Banner, Backwall and Desk Wrap - Design

Must have by Monday 12th 8am Sydney Time.
We need two Banner designs to meet attached specs.
We need one wall design to meet attached specs.
We need one desk wrap design to meet attached specs.

The wall banner can be based off the two separate banners - am open to ideas on this

We are a Cloud telephony and internet provider. Our Websites are
www.brevalink.com.au
www.tarnovia.com.au
Banners will be created under the Brevalink brand

I have included a word document with some ideas - but please be creative as I'm not a designer.

Theme must carry across all banners as they are for trade shows

I have also included the following - sample cloud backgrounds (you do not have to use them - if you have a better idea) - a sample business card we use - Two sample logos - square and horizontal.
A Quorra Perks logo - unfortunately I do not have this graphic in high quality so it will have to be redesigned. It doesn't have to match
Desktop Wrap will be logo and background

Notes from Questions Asked
1) The deskwrap spcs are in the file called Graphic Wall Skirt
2) There will be Two separate Banners with Content from Word Doc. One will be based around VoIP and the other around Internet. Background Wall can be a combination of the banners laid out in a professional manner.

Apologies to all: The Printwell Yard has now supplied me the correct measurements in PDFs these have now been uploaded

Target Market(s)

Small to Medium Business Market

Requirements
Must have
• Must have designs for decision on Monday 8am Sydney Time to meet trade show
Nice to have
• Want Both Banner to be similar in design. Carry banner designs across to the back wall

```html
<!DOCTYPE html>
<html lang="en">
<head>
<meta charset="utf-8">
<title>Brevalink – Trade Show Wall, Desk Wrap and Banners</title>
<link href="https://fonts.googleapis.com/css2?family=Open+Sans:wght@400;600;700&family=Roboto:wght@500;700&display=swap" rel="stylesheet">
<style>
  :root{
    --sky-deep:#1577d4;
    --sky-mid:#2f8ee0;
    --sky-light:#6cbaf0;
    --white:#ffffff;
    --brand-grey:#4b4f55;
    --brand-dot:#4fc3ec;
    --guide:#b5b5b5;
    --node-red:#c8473f;
    --node-orange:#d6813f;
    --node-tan:#c9a14f;
    --node-olive:#a9b94a;
    --node-hub:#3d7cc6;
    --arrow:#e9a94a;
  }
  *{margin:0;padding:0;box-sizing:border-box}
  html,body{width:1014px;height:1200px;overflow:hidden;background:var(--white)}
  .canvas{position:relative;width:1014px;height:1200px}

  .sky{position:absolute;
    background:
      radial-gradient(ellipse 40% 6% at 25% 12%, rgba(255,255,255,.22), transparent 70%),
      radial-gradient(ellipse 35% 5% at 75% 30%, rgba(255,255,255,.18), transparent 70%),
      radial-gradient(ellipse 45% 6% at 40% 72%, rgba(255,255,255,.2), transparent 70%),
      radial-gradient(ellipse 30% 5% at 85% 85%, rgba(255,255,255,.16), transparent 70%),
      linear-gradient(180deg,var(--sky-mid) 0%,var(--sky-deep) 45%,var(--sky-light) 100%);}
  .sky--tall{
    background:
      radial-gradient(ellipse 60% 3% at 40% 8%, rgba(255,255,255,.2), transparent 70%),
      radial-gradient(ellipse 60% 3% at 60% 60%, rgba(255,255,255,.15), transparent 70%),
      linear-gradient(180deg,var(--sky-mid) 0%,var(--sky-deep) 50%,var(--sky-light) 85%,var(--sky-deep) 100%);}

  .brand{position:absolute;left:0;right:0;display:flex;align-items:center;justify-content:center;gap:.35em;
    font-family:"Open Sans",sans-serif;font-weight:700;color:var(--brand-grey)}
  .brand__dot{width:.55em;height:.55em;border-radius:50%;background:var(--brand-dot)}

  .strapline{position:absolute;left:0;right:0;text-align:center;font-family:"Roboto",sans-serif;font-weight:700;color:var(--brand-grey);letter-spacing:.02em}
  .tagline{position:absolute;left:0;right:0;text-align:center;font-family:"Roboto",sans-serif;font-weight:700;color:var(--white);line-height:1.2}

  /* back wall */
  .backwall{position:absolute;left:50px;top:0;width:932px;height:586px;overflow:hidden}
  .backwall .brand{top:170px;font-size:64px}
  .backwall .strapline{top:280px;font-size:14px}
  .backwall .tagline{top:316px;font-size:22px}

  /* desk wrap */
  .deskwrap__guide{position:absolute;left:186px;top:646px;width:222px;height:553px;border:1px dotted var(--guide)}
  .deskwrap{position:absolute;left:0;top:724px;width:476px;height:212px;overflow:hidden}
  .deskwrap .brand{top:92px;font-size:34px}
  .deskwrap .strapline{top:156px;font-size:8px}
  .deskwrap .tagline{top:173px;font-size:9px}

  /* pull-up banners */
  .banner{position:absolute;top:626px;width:221px;height:552px;overflow:hidden}
  .banner--internet{left:529px}
  .banner--voip{left:793px;top:625px}
  .banner .brand{top:110px;font-size:30px}
  .banner__services{position:absolute;left:0;right:0;top:154px;text-align:center;font-family:"Open Sans",sans-serif;font-size:10.5px;color:var(--brand-grey)}
  .banner__phone{position:absolute;left:0;right:0;top:172px;text-align:center;font-family:"Open Sans",sans-serif;font-weight:600;font-size:20px;color:var(--white);line-height:1}
  .banner__digits{position:absolute;left:0;right:0;top:193px;text-align:center;font-family:"Open Sans",sans-serif;font-size:11px;letter-spacing:.45em;color:var(--white);padding-left:50px}
  .banner__points{position:absolute;left:36px;right:6px;list-style:none;font-family:"Open Sans",sans-serif;font-weight:600;font-size:13.5px;color:var(--white);line-height:1.1}
  .banner__points li{position:relative;padding-left:7px;margin-bottom:5px}
  .banner__points li::before{content:"";position:absolute;left:0;top:.5em;width:4px;height:4px;border-radius:50%;background:var(--white)}
  .banner--internet .banner__points{top:217px;left:36px}
  .banner--voip .banner__points{top:213px;left:27px;font-size:13px}
  .banner--voip .banner__points li{margin-bottom:3px}
  .banner__diagram{position:absolute;left:0;top:0;width:221px;height:552px}
  .banner__save{position:absolute;left:30px;top:440px;font-family:"Open Sans",sans-serif;font-weight:600;font-size:12px;color:var(--white)}
  .banner__offer{position:absolute;left:0;right:0;top:452px;text-align:center;font-family:"Open Sans",sans-serif;font-weight:700;font-size:21px;letter-spacing:.05em;color:var(--white)}
  .banner .tagline{top:490px;font-size:11.5px}

  .node-label{font-family:"Open Sans",sans-serif;font-weight:700;fill:var(--white);text-anchor:middle}
</style>
</head>
<body>
<div class="canvas">

  <!-- Back wall -->
  <section class="backwall sky" role="img" aria-label="Blue sky with soft white clouds">
    <div class="brand"><span class="brand__dot"></span>Brevalink</div>
    <div class="strapline">PHONES - DATA - INTERNET</div>
    <div class="tagline">Helping Business Communicate<br>for over 25 Years</div>
  </section>

  <!-- Desk wrap -->
  <div class="deskwrap__guide"></div>
  <section class="deskwrap sky" role="img" aria-label="Blue sky with soft white clouds">
    <div class="brand"><span class="brand__dot"></span>Brevalink</div>
    <div class="strapline">PHONES - DATA - INTERNET</div>
    <div class="tagline">Helping Business Communicate<br>for over 25 Years</div>
  </section>

  <!-- Internet banner -->
  <section class="banner banner--internet sky sky--tall" role="img" aria-label="Blue sky with soft white clouds">
    <div class="brand"><span class="brand__dot"></span>Brevalink</div>
    <div class="banner__services">Internet | Fibre | NBN | VoIP</div>
    <div class="banner__phone">1300 BREVA 1</div>
    <div class="banner__digits">(273821)</div>
    <ul class="banner__points">
      <li>Internet to Suit You</li>
      <li>Carrier Grade SLA’s</li>
      <li>No Nonsense Support</li>
    </ul>
    <svg class="banner__diagram" viewBox="0 0 221 552">
      <defs>
        <marker id="arrow-internet" viewBox="0 0 10 10" refX="5" refY="5" markerWidth="5" markerHeight="5" orient="auto"><path d="M0 0 L10 5 L0 10z" fill="var(--arrow)"/></marker>
      </defs>
      <g stroke="var(--arrow)" stroke-width="2" marker-end="url(#arrow-internet)">
        <line x1="110" y1="328" x2="110" y2="322"/>
        <line x1="129" y1="340" x2="136" y2="335"/>
        <line x1="129" y1="360" x2="137" y2="366"/>
        <line x1="110" y1="372" x2="110" y2="380"/>
        <line x1="91" y1="360" x2="83" y2="366"/>
        <line x1="91" y1="340" x2="84" y2="335"/>
      </g>
      <circle cx="110" cy="302" r="19" fill="var(--node-red)"/>
      <circle cx="162" cy="325" r="19" fill="var(--node-orange)"/>
      <circle cx="166" cy="377" r="19" fill="var(--node-orange)"/>
      <circle cx="110" cy="410" r="22" fill="var(--node-tan)"/>
      <circle cx="54" cy="377" r="21" fill="var(--node-olive)"/>
      <circle cx="58" cy="325" r="19" fill="var(--node-olive)"/>
      <circle cx="110" cy="350" r="21" fill="var(--node-hub)"/>
      <text class="node-label" x="110" y="306" font-size="10">NBN</text>
      <text class="node-label" x="162" y="324" font-size="5">Multisite</text>
      <text class="node-label" x="162" y="330" font-size="5">Connectivity</text>
      <text class="node-label" x="166" y="376" font-size="6">Metro</text>
      <text class="node-label" x="166" y="383" font-size="6">Ethernet</text>
      <text class="node-label" x="110" y="409" font-size="6">Fibre</text>
      <text class="node-label" x="110" y="416" font-size="6">Connections</text>
      <text class="node-label" x="54" y="380" font-size="9" font-weight="400">VoIP</text>
      <text class="node-label" x="58" y="324" font-size="6">Multi</text>
      <text class="node-label" x="58" y="331" font-size="6">Vendor</text>
      <text class="node-label" x="110" y="354" font-size="10" font-weight="600">Internet</text>
    </svg>
    <div class="banner__save">Save Now!</div>
    <div class="banner__offer">FREE ANALYSIS</div>
    <div class="tagline">Helping Business Communicate<br>for over 25 Years</div>
  </section>

  <!-- VoIP banner -->
  <section class="banner banner--voip sky sky--tall" role="img" aria-label="Blue sky with soft white clouds">
    <div class="brand"><span class="brand__dot"></span>Brevalink</div>
    <div class="banner__services">Internet | Cloud | Voice</div>
    <div class="banner__phone">1300 BREVA 1</div>
    <div class="banner__digits">(273821)</div>
    <ul class="banner__points">
      <li>Reduce your Telephone Costs Instantly</li>
      <li>Transition to VoIP</li>
      <li>Full Featured Hosted PBX</li>
    </ul>
    <svg class="banner__diagram" viewBox="0 0 221 552">
      <defs>
        <marker id="arrow-voip" viewBox="0 0 10 10" refX="5" refY="5" markerWidth="5" markerHeight="5" orient="auto"><path d="M0 0 L10 5 L0 10z" fill="var(--arrow)"/></marker>
      </defs>
      <g stroke="var(--arrow)" stroke-width="2" marker-end="url(#arrow-voip)">
        <line x1="110" y1="341" x2="110" y2="335"/>
        <line x1="129" y1="352" x2="136" y2="347"/>
        <line x1="129" y1="372" x2="137" y2="378"/>
        <line x1="110" y1="384" x2="110" y2="392"/>
        <line x1="91" y1="372" x2="83" y2="378"/>
        <line x1="91" y1="352" x2="84" y2="347"/>
      </g>
      <circle cx="110" cy="315" r="19" fill="var(--node-red)"/>
      <circle cx="164" cy="338" r="19" fill="var(--node-orange)"/>
      <circle cx="167" cy="388" r="21" fill="var(--node-orange)"/>
      <circle cx="110" cy="416" r="22" fill="var(--node-tan)"/>
      <circle cx="54" cy="388" r="21" fill="var(--node-olive)"/>
      <circle cx="58" cy="338" r="19" fill="var(--node-olive)"/>
      <circle cx="110" cy="362" r="21" fill="var(--node-hub)"/>
      <text class="node-label" x="110" y="314" font-size="5">IVR and Call</text>
      <text class="node-label" x="110" y="320" font-size="5">Recording</text>
      <text class="node-label" x="164" y="340" font-size="5.5">Fax to Email</text>
      <text class="node-label" x="167" y="387" font-size="6">Mobile</text>
      <text class="node-label" x="167" y="394" font-size="6">Phones</text>
      <text class="node-label" x="110" y="415" font-size="6">Remote</text>
      <text class="node-label" x="110" y="422" font-size="6">Home Office</text>
      <text class="node-label" x="54" y="387" font-size="5">Office</text>
      <text class="node-label" x="54" y="393" font-size="5">Phones</text>
      <text class="node-label" x="58" y="336" font-size="5">Remote</text>
      <text class="node-label" x="58" y="342" font-size="5">Branch PBX</text>
      <text class="node-label" x="110" y="367" font-size="13" font-weight="600">PBX</text>
    </svg>
    <div class="banner__offer">FREE ANALYSIS</div>
    <div class="tagline">Helping Business Communicate<br>for over 25 Years</div>
  </section>

</div>
</body>
</html>
```